The most modern business card ever !!!

Our company call “Vantilo”. Vantilo is a technology company specialized in cruises solutions. Out main product is a platform to reserve cruises. This is a revolutionary platform that make easier to travel agencies and final users to reserve cruises across dozen companies like tarvik, welbi, dpv, hbt, etc..We are a “start up”, with a young team of developers and we want to transmit it.. For it, we want something different, a modern business card that represent cruises and technology.. When someone receive this card, this person should say: wowww this is different… this is modern… this is a cruise related company..
Contact Information for Business Card
Requirements
Must have
- diferent, modern
Should not have
- traditions business card

```html
<!DOCTYPE html>
<html lang="en">
<head>
<meta charset="utf-8">
<title>Vantilo Business Card</title>
<link href="https://fonts.googleapis.com/css2?family=Exo+2:wght@400;600;700&display=swap" rel="stylesheet">
<style>
  :root {
    --backdrop: #5a5a5a;
    --card-white: #ffffff;
    --ink: #0d0d0d;
    --sky: #29a8e0;
    --mist: #e6e6e6;
    --on-sky: #ffffff;
  }
  * { margin: 0; padding: 0; box-sizing: border-box; }
  html, body { width: 1200px; height: 802px; overflow: hidden; }
  body {
    background: var(--backdrop);
    font-family: "Exo 2", sans-serif;
    position: relative;
  }
  .card {
    position: absolute;
    top: 274px;
    width: 443px;
    height: 265px;
    background: var(--card-white);
    overflow: hidden;
    box-shadow: 0 3px 6px rgba(0,0,0,0.35);
  }
  .card-front { left: 136px; }
  .card-back { left: 624px; }

  .ink-band {
    position: absolute;
    left: 53px;
    top: 0;
    width: 26px;
    height: 100%;
    background: var(--ink);
  }
  .sky-panel {
    position: absolute;
    left: 100px;
    top: 0;
    right: 0;
    height: 100%;
    background: var(--sky);
  }
  .mist-band {
    position: absolute;
    left: 0;
    top: 0;
    width: 44px;
    height: 100%;
    background: var(--mist);
  }

  .contact-block {
    position: absolute;
    right: 22px;
    top: 60px;
    text-align: right;
    color: var(--on-sky);
  }
  .holder-name { font-weight: 700; font-size: 16.5px; letter-spacing: 0.3px; line-height: 1; }
  .holder-role { font-size: 12.5px; line-height: 1.1; margin-top: 1px; }
  .contact-list { list-style: none; margin-top: 12px; font-size: 12px; line-height: 16px; }
  .contact-list li { display: flex; justify-content: flex-end; align-items: center; gap: 3px; }
  .contact-list svg { width: 10px; height: 10px; fill: var(--on-sky); }
  .postal { margin-top: 9px; font-size: 12px; line-height: 16px; font-style: normal; }

  .brand-name {
    position: absolute;
    left: 109px;
    top: 106px;
    font-weight: 600;
    font-size: 54px;
    line-height: 1;
    letter-spacing: 3px;
    color: var(--ink);
  }
</style>
</head>
<body>

<section class="card card-front">
  <div class="ink-band"></div>
  <div class="sky-panel"></div>
  <div class="contact-block">
    <p class="holder-name">DANIEL ORVEN</p>
    <p class="holder-role">Managing Director</p>
    <ul class="contact-list">
      <li>044-318 270 645
        <svg viewBox="0 0 10 10"><path d="M1 4c0-2 2-3 4-3s4 1 4 3H7V3H3v1zM2 5h6l1 4H1z"/></svg></li>
      <li>044-318 270 645
        <svg viewBox="0 0 10 10"><path d="M2.5 0h5v10h-5zM3.3 1v7h3.4V1z"/></svg></li>
      <li>hello@vantilomail.com
        <svg viewBox="0 0 10 10"><path d="M0 2h10v6H0zM1 3l4 3 4-3z" fill-rule="evenodd"/></svg></li>
      <li>www.vantilocruise.com
        <svg viewBox="0 0 10 10"><circle cx="5" cy="5" r="4.5"/></svg></li>
    </ul>
    <address class="postal">12345, Address Goes Here<br>Country Name, 123456</address>
  </div>
</section>

<section class="card card-back">
  <div class="mist-band"></div>
  <p class="brand-name">Vantilo</p>
</section>

</body>
</html>
```